Fast Growing Personal Injury Law Firm Needs Business Card Design

We need a business card design for a fast growing personal injury law firm in Florida. Our name is Darren Kolvisty, P.A. Our practice is comprised of younger attorneys (in their 30s) that employ more modern techniques/tools than our older competition. We would prefer a look that is a modern play on a classic look. Also, we would like to continue using a color scheme that employs navy blue and kelly green (other shades of green could be fine too) as well as our "E" logo.

Industry/Entity Type

Law Firm

```html
<!DOCTYPE html>
<html lang="en">
<head>
<meta charset="utf-8">
<title>Darren Kolvisty, P.A. – Business Card</title>
<link rel="stylesheet" href="https://fonts.googleapis.com/css2?family=Merriweather:ital,wght@0,400;0,700;0,900;1,400&display=swap">
<style>
  :root {
    --navy: #1b3a8c;
    --navy-deep: #14296a;
    --green: #2fa336;
    --green-light: #5cbf3a;
    --blue: #1f63c8;
    --paper: #ffffff;
    --ink: #33405e;
    --stage: #e9e9eb;
  }
  * { box-sizing: border-box; margin: 0; padding: 0; }
  html, body { width: 1200px; height: 768px; overflow: hidden; }
  body {
    background: var(--stage);
    font-family: "Merriweather", Georgia, serif;
    position: relative;
  }
  .card {
    position: absolute;
    top: 229px;
    width: 540px;
    height: 310px;
    background: var(--paper);
    overflow: hidden;
    box-shadow: 0 2px 10px rgba(0,0,0,0.12);
  }
  .card--back { left: 40px; }
  .card--front { left: 620px; }

  .card-band { position: absolute; left: 0; bottom: 0; width: 100%; height: 40px; }

  /* back */
  .back-mark {
    position: absolute; left: 0; right: 0; top: 100px;
    display: flex; flex-direction: column; align-items: center; gap: 14px;
  }
  .mark-square {
    width: 58px; height: 58px;
    background: var(--navy);
  }
  .back-name {
    font-size: 24px; font-weight: 700; color: var(--navy);
  }

  /* front */
  .front-head { position: absolute; left: 26px; top: 24px; display: flex; gap: 14px; }
  .front-head .mark-square { width: 62px; height: 62px; flex: none; }
  .firm-name { font-size: 25px; font-weight: 900; color: var(--navy); line-height: 1.15; margin-top: 22px; }
  .firm-tagline { font-size: 20px; font-weight: 700; color: var(--green); letter-spacing: 1.2px; line-height: 1.2; }

  .contact { position: absolute; left: 26px; top: 112px; color: var(--ink); }
  .contact-name { font-size: 14px; font-weight: 700; color: var(--navy); }
  .contact-role { font-size: 10px; font-style: italic; margin-bottom: 6px; }
  .contact-list { list-style: none; font-size: 11px; line-height: 1.55; }
  .contact-list li { display: flex; align-items: center; gap: 7px; }
  .contact-list svg { width: 11px; height: 11px; fill: var(--green); flex: none; }
  .contact-address { font-size: 10px; line-height: 1.45; margin-top: 3px; }

  .portrait {
    position: absolute; right: 22px; bottom: 22px;
    width: 200px; height: 150px;
    background: linear-gradient(180deg, #f2f2f2 0%, #c9b6a6 45%, #2a2d36 75%, #1c1e25 100%);
  }
</style>
</head>
<body>

<section class="card card--back">
  <div class="back-mark">
    <div class="mark-square"></div>
    <div class="back-name">Darren Kolvisty, P.A.</div>
  </div>
  <svg class="card-band" viewBox="0 0 540 40" preserveAspectRatio="none">
    <polygon points="0,30 300,30 318,40 0,40" fill="var(--green)"/>
    <polygon points="300,30 540,30 540,40 318,40" fill="var(--blue)"/>
  </svg>
</section>

<section class="card card--front">
  <header class="front-head">
    <div class="mark-square"></div>
    <div>
      <div class="firm-name">Darren Kolvisty, P.A.</div>
      <div class="firm-tagline">Personal Injury Attorneys</div>
    </div>
  </header>

  <div class="contact">
    <div class="contact-name">Darren Kolvisty</div>
    <div class="contact-role">Attorney at Law</div>
    <ul class="contact-list">
      <li><svg viewBox="0 0 12 12"><path d="M2 1h3l1 3-1.5 1a6 6 0 0 0 2.5 2.5L8 6l3 1v3a1 1 0 0 1-1 1A9 9 0 0 1 1 2a1 1 0 0 1 1-1z"/></svg>941 555 0182</li>
      <li><svg viewBox="0 0 12 12"><path d="M3 1h6v3H3zM1 5h10v5H9v1H3v-1H1zM4 8v2h4V8z"/></svg>941 555 0147</li>
      <li><svg viewBox="0 0 12 12"><path d="M1 2h10v8H1zM2 3v.5L6 6l4-2.5V3z"/></svg>darren@kolvistylaw.com</li>
      <li><svg viewBox="0 0 12 12"><circle cx="6" cy="6" r="5"/></svg>www.kolvistylaw.com</li>
    </ul>
    <div class="contact-address">2150 Harbor View Drive Suite 210<br>Palm Crest, Florida 34299</div>
  </div>

  <div class="portrait" role="img" aria-label="Portrait photograph of the attorney in a dark suit and tie"></div>

  <svg class="card-band" viewBox="0 0 540 40" preserveAspectRatio="none">
    <polygon points="0,30 300,30 318,40 0,40" fill="var(--green)"/>
    <polygon points="300,30 540,30 540,40 318,40" fill="var(--blue)"/>
  </svg>
</section>

</body>
</html>
```